Visitenkarten-Design für Versicherungsmakler
Zielgruppe
Wir sind ein Versicherungsmakler aus Leipzig.
Aufgabenstellung
Im Anhang finden Sie die alte Visitenkarte. Die Daten können übernommen werden. Aber statt Inhaber bitte 'Geschäftsführer'
Die Farben sollten beibehalten werden. Bei der Frage ob das rot oder das grau die Primärfarbe ist, bin ich flexibel. Von der Gestaltung her sind Ihnen ansonsten keine Grenzen gesetzt.

```html
<!DOCTYPE html>
<html lang="de">
<head>
<meta charset="utf-8">
<title>Visitenkarte veltaro</title>
<link rel="stylesheet" href="https://fonts.googleapis.com/css2?family=Open+Sans:wght@400;600&display=swap">
<style>
  :root {
    --brand-red: #c8202f;
    --text-grey: #6b6b6b;
    --line-grey: #d9d9d9;
    --card-white: #ffffff;
    --backdrop: #2b2725;
  }
  * { margin: 0; padding: 0; box-sizing: border-box; }
  html, body { width: 1200px; height: 900px; overflow: hidden; }
  body {
    background: var(--backdrop);
    font-family: "Open Sans", Arial, sans-serif;
    position: relative;
  }
  .card {
    position: absolute;
    width: 510px;
    height: 300px;
    background: var(--card-white);
    box-shadow: 0 10px 30px rgba(0,0,0,.45);
    overflow: hidden;
  }
  .card--front { left: 60px; top: 300px; }
  .card--back { left: 630px; top: 300px; }

  /* front */
  .front__brand {
    position: absolute; right: 34px; top: 30px;
    color: var(--brand-red); font-size: 42px; font-weight: 400; letter-spacing: .5px;
  }
  .front__person { position: absolute; right: 60px; top: 128px; text-align: center; }
  .person__name { color: var(--brand-red); font-size: 22px; font-weight: 400; }
  .person__role { color: var(--text-grey); font-size: 13px; margin-top: 2px; }
  .contact-list {
    position: absolute; left: 32px; top: 134px; list-style: none;
    color: var(--text-grey); font-size: 13.5px; line-height: 1.35;
  }
  .contact-list li { display: flex; align-items: flex-start; gap: 10px; margin-bottom: 4px; }
  .contact-list svg { flex: none; width: 15px; height: 15px; margin-top: 2px; }
  .front__band {
    position: absolute; left: 0; right: 0; bottom: 0; height: 14px; background: var(--brand-red);
  }

  /* back */
  .back__brand {
    position: absolute; left: 0; right: 0; top: 92px; text-align: center;
    color: var(--brand-red); font-size: 64px; font-weight: 400; letter-spacing: 1px;
  }
  .back__rule {
    position: absolute; left: 24px; right: 24px; height: 1px; background: var(--brand-red); opacity: .6;
  }
  .back__rule--top { bottom: 64px; }
  .back__rule--bottom { bottom: 14px; }
  .legal {
    position: absolute; left: 24px; right: 24px; bottom: 22px; text-align: center;
    color: var(--text-grey); font-size: 9.5px; line-height: 1.5;
  }
</style>
</head>
<body>

<section class="card card--front" aria-label="Visitenkarte Vorderseite">
  <div class="front__brand">veltaro</div>
  <div class="front__person">
    <div class="person__name">Lukas BRANDT</div>
    <div class="person__role">Geschäftsführer</div>
  </div>
  <ul class="contact-list">
    <li>
      <svg viewBox="0 0 16 16"><circle cx="8" cy="8" r="8" fill="var(--brand-red)"/><path d="M8 3.5a3 3 0 0 0-3 3c0 2.2 3 5.5 3 5.5s3-3.3 3-5.5a3 3 0 0 0-3-3z" fill="#fff"/><circle cx="8" cy="6.5" r="1.1" fill="var(--brand-red)"/></svg>
      <span>Lindenweg<br>48 09876 Altenbrück</span>
    </li>
    <li>
      <svg viewBox="0 0 16 16"><circle cx="8" cy="8" r="8" fill="var(--brand-red)"/><path d="M5 4.2l1.6-.4 1 2.2-1 .8a5 5 0 0 0 2.6 2.6l.8-1 2.2 1-.4 1.6c-3.8.2-7-3-6.8-6.8z" fill="#fff"/></svg>
      <span>0341-55012740</span>
    </li>
    <li>
      <svg viewBox="0 0 16 16"><circle cx="8" cy="8" r="8" fill="var(--brand-red)"/><rect x="4.5" y="6" width="7" height="5" fill="#fff"/><rect x="5.5" y="4" width="5" height="2" fill="#fff"/></svg>
      <span>0341-55012749</span>
    </li>
    <li>
      <svg viewBox="0 0 16 16"><circle cx="8" cy="8" r="8" fill="var(--brand-red)"/><rect x="5.5" y="3.5" width="5" height="9" rx="1" fill="#fff"/></svg>
      <span>0172-8841306</span>
    </li>
    <li>
      <svg viewBox="0 0 16 16"><circle cx="8" cy="8" r="8" fill="var(--brand-red)"/><rect x="4" y="5" width="8" height="6" fill="#fff"/><path d="M4 5l4 3.2L12 5" stroke="var(--brand-red)" stroke-width=".9" fill="none"/></svg>
      <span>lukas.brandt@veltaro.de</span>
    </li>
    <li>
      <svg viewBox="0 0 16 16"><circle cx="8" cy="8" r="8" fill="var(--brand-red)"/><circle cx="8" cy="8" r="4" fill="none" stroke="#fff" stroke-width="1"/><path d="M4 8h8M8 4c-2 2.5-2 5.5 0 8M8 4c2 2.5 2 5.5 0 8" stroke="#fff" stroke-width=".8" fill="none"/></svg>
      <span>www.veltaro.de</span>
    </li>
  </ul>
  <div class="front__band"></div>
</section>

<section class="card card--back" aria-label="Visitenkarte Rückseite">
  <div class="back__brand">veltaro</div>
  <div class="back__rule back__rule--top"></div>
  <p class="legal">
    Freier Versicherungsmakler mit Erlaubnis nach § 34d Abs. 1 GewO<br>
    - Erlaubnisbehörde: Gewerbekammer Altenbrück, Marktstraße 12, 09870 Altenbrück - Reg.-Nr. D-4KTR-M27PL-31
  </p>
  <div class="back__rule back__rule--bottom"></div>
</section>

</body>
</html>
```